Extremely Professional Lawyer needs letterhead for new boutique real estate law firm

I need letterhead for my new solo practice law firm. I practiced as a partner in a huge global law firm for years. Now I am starting a solo firm where I will deliver very high-quality legal services that are real-estate focused. The idea is that my practice will be very focused but that the services will be at the quality level provided by partners at high-profile law firms. The name of my law firm will be Brenn Law Group, LLC. For now, I am the only lawyer. I expect to negotiate and draft house sale/purchase contracts and close house deals. Eventually, I would like to do small-scale development deals for developer clients, a specialty of mine.

Industry/Entity Type

Boutique

```html
<!DOCTYPE html>
<html lang="en">
<head>
<meta charset="utf-8">
<title>Brenn Law Group, LLC – Letterhead</title>
<link rel="stylesheet" href="https://fonts.googleapis.com/css2?family=Arimo:wght@400;700&display=swap">
<style>
  :root {
    --paper: #ffffff;
    --ink: #2b2b2b;
    --navy: #1b3f7f;
    --muted: #3a3a3a;
  }
  html, body {
    margin: 0;
    padding: 0;
    overflow: hidden;
    background: var(--paper);
  }
  .letterhead {
    position: relative;
    width: 849px;
    height: 1200px;
    background: var(--paper);
    color: var(--ink);
    font-family: "Arimo", Arial, sans-serif;
    overflow: hidden;
  }
  .brand {
    position: absolute;
    left: 530px;
    top: 95px;
    display: flex;
    align-items: center;
    gap: 14px;
  }
  .brand-square {
    width: 52px;
    height: 52px;
    background: var(--navy);
  }
  .brand-name {
    color: var(--navy);
    font-weight: 700;
    line-height: 1;
  }
  .brand-name .primary {
    display: block;
    font-size: 46px;
  }
  .brand-name .secondary {
    display: block;
    font-size: 15px;
    margin-top: 4px;
  }
  .contact {
    position: absolute;
    left: 533px;
    top: 182px;
    font-size: 14px;
    line-height: 21px;
    color: var(--muted);
    margin: 0;
  }
  .contact dt {
    float: left;
    clear: left;
    width: 52px;
  }
  .contact dd {
    margin: 0 0 0 52px;
  }
  .contact-rule {
    position: absolute;
    left: 700px;
    top: 340px;
    width: 128px;
    height: 8px;
    background: var(--navy);
  }
  .letter {
    position: absolute;
    left: 60px;
    top: 380px;
    width: 725px;
    font-size: 14px;
    line-height: 22px;
    color: var(--ink);
  }
  .date { margin: 0 0 48px; }
  .salutation { margin: 0 0 20px; font-size: 17px; }
  .letter-body p { margin: 0 0 22px; text-align: justify; }
  .closing { margin: 36px 0 8px; }
  .signature {
    width: 170px;
    height: 52px;
    background: linear-gradient(90deg, #cfcfcf, #e6e6e6);
  }
  .signer { margin: 6px 0 0; }
</style>
</head>
<body>
<main class="letterhead">
  <header>
    <div class="brand">
      <span class="brand-square"></span>
      <span class="brand-name">
        <span class="primary">Brenn</span>
        <span class="secondary">Law Group, LLC.</span>
      </span>
    </div>
    <dl class="contact">
      <dt>NO.</dt><dd>: 418 Harmon Street,</dd>
      <dt>&nbsp;</dt><dd>&nbsp;&nbsp;Suite 1200,</dd>
      <dt>&nbsp;</dt><dd>&nbsp;&nbsp;Chicago, IL 60601</dd>
      <dt>TEL</dt><dd>: 000-000-0000</dd>
      <dt>WEB</dt><dd>: www.brennlaw.com</dd>
      <dt>email</dt><dd>: office@brennlaw.com</dd>
    </dl>
    <div class="contact-rule"></div>
  </header>

  <article class="letter">
    <p class="date">May 21-05-2014</p>
    <p class="salutation">Dear Client,</p>
    <div class="letter-body">
      <p>Thank you for choosing Brenn Law Group to guide you through the purchase of your new home. Our practice is focused entirely on residential and development real estate, and we bring to every file the care and precision you would expect from partners at the largest firms. Over the coming weeks we will review the contract of sale, coordinate with your lender and title company, and resolve any questions that arise before closing. You will receive a written summary at each stage so that nothing is left to chance.</p>
      <p>Please gather the documents listed on the enclosed checklist and return them at your earliest convenience. Early delivery allows us to keep your closing date firmly on schedule.</p>
      <p>Should you have any questions, do not hesitate to call or write to our office. We are available to meet in person or by video at a time that suits you, and we will respond to every message within one business day. It is a privilege to represent you, and we look forward to a smooth and successful closing.</p>
    </div>
    <p class="closing">yours sincerely,</p>
    <div class="signature" role="img" aria-label="Handwritten signature of Dana Brenn"></div>
    <p class="signer">Dana Brenn</p>
  </article>
</main>
</body>
</html>
```